Oil Field Service company needs professional business cards

Looking to clean up our current company business cards and look a little more professional. Harlow Casing Services is a US based company that services the oil field. We deal with engineers, managers and oil rigs....................................................................................................................................................................................................................................................................................................................................................................................................

Target Market(s)

Oil and Gas professionals

Industry/Entity Type

Oil And Gas

Contact Information for Business Card

See attached photo as example

Font styles to use
Sans Serif

Colors
ec1f27

Requirements
Must have
• Company Logo, Name, Title, Cell, Office, Fax, Email.
• See attached photo
Nice to have
• External CRT, Internal CRT, Casing Crews, Torque Turn, Laydown Machine
Should not have
• Do not introduce any new pictures and keep it professional looking

```html
<!DOCTYPE html>
<html lang="en">
<head>
<meta charset="utf-8">
<title>Harlow Casing Services – Business Card</title>
<link rel="stylesheet" href="https://fonts.googleapis.com/css2?family=Oswald:wght@400&family=Roboto:wght@400;700&family=Roboto+Condensed:wght@400&display=swap">
<style>
  :root {
    --backdrop: #e4e4e4;
    --brand-red: #d0211f;
    --brand-red-dark: #c01c1b;
    --card-white: #f7f7f7;
    --slate: #3e4f60;
    --ink: #3a3a3a;
    --ink-soft: #555555;
  }
  * { margin: 0; padding: 0; box-sizing: border-box; }
  html, body {
    width: 1200px; height: 576px; overflow: hidden;
    background: var(--backdrop);
  }
  .canvas { position: relative; width: 1200px; height: 576px; }

  .card {
    position: absolute; top: 139px;
    width: 484px; height: 293px;
    border-radius: 7px; overflow: hidden;
  }

  /* Front */
  .card-front {
    left: 82px;
    background: linear-gradient(180deg, var(--brand-red) 0%, var(--brand-red-dark) 100%);
    display: flex; align-items: center; justify-content: center;
  }
  .front-wordmark {
    font-family: "Roboto", sans-serif; font-weight: 700;
    font-size: 30px; letter-spacing: 0.5px;
    color: #ffffff;
  }

  /* Back */
  .card-back { left: 602px; background: var(--card-white); }
  .back-wordmark {
    position: absolute; top: 56px; right: 24px;
    font-family: "Roboto", sans-serif; font-weight: 700;
    font-size: 22px; letter-spacing: 0.4px;
    color: var(--slate);
  }
  .name-tab {
    position: absolute; left: 0; top: 165px;
    width: 11px; height: 42px;
    background: var(--brand-red);
    border-radius: 0 21px 21px 0;
  }
  .person { position: absolute; left: 24px; top: 164px; }
  .person-name {
    font-family: "Oswald", sans-serif; font-weight: 400;
    font-size: 22px; line-height: 26px; color: var(--ink);
  }
  .person-title {
    font-family: "Roboto", sans-serif; font-size: 11px;
    color: var(--ink-soft); margin-top: 1px;
  }

  .contact-grid {
    position: absolute; left: 24px; top: 235px;
    display: grid;
    grid-template-columns: 109px 125px auto;
    row-gap: 3px;
    font-family: "Roboto Condensed", sans-serif; font-size: 12px;
    color: var(--ink);
  }
  .contact-item { display: flex; align-items: center; gap: 9px; line-height: 13px; }
  .contact-item svg { width: 10px; height: 10px; fill: var(--brand-red); flex: none; }
</style>
</head>
<body>
<main class="canvas">

  <section class="card card-front" aria-label="Business card front">
    <span class="front-wordmark">Harlow Casing Services</span>
  </section>

  <section class="card card-back" aria-label="Business card back">
    <span class="back-wordmark">Harlow Casing Services</span>

    <div class="name-tab"></div>
    <div class="person">
      <div class="person-name">Casey Landry</div>
      <div class="person-title">Area Manager</div>
    </div>

    <div class="contact-grid">
      <div class="contact-item">
        <svg viewBox="0 0 10 10" aria-label="Cell"><path d="M2 0.5h2l1 2.4-1.3 1a5.5 5.5 0 0 0 2.4 2.4l1-1.3 2.4 1v2A1.5 1.5 0 0 1 8 9.5 7.5 7.5 0 0 1 0.5 2 1.5 1.5 0 0 1 2 0.5z"/></svg>
        (555) 014-2200
      </div>
      <div class="contact-item">
        <svg viewBox="0 0 10 10" aria-label="Fax"><rect x="2.5" y="0.5" width="5" height="2.5"/><rect x="0.5" y="3.5" width="9" height="4" rx="0.8"/><rect x="2.5" y="6.5" width="5" height="3"/></svg>
        (555) 014-2231
      </div>
      <div class="contact-item">
        <svg viewBox="0 0 10 10" aria-label="Email"><path d="M0.5 2h9v6h-9z M0.5 2l4.5 3.5L9.5 2" fill="var(--brand-red)"/><path d="M1 2.3l4 3.1 4-3.1" stroke="#fff" stroke-width="0.8" fill="none"/></svg>
        caseylandry@harlowsrvs.com
      </div>

      <div class="contact-item">
        <svg viewBox="0 0 10 10" aria-label="Office"><path d="M0.5 3.5C2 1.5 8 1.5 9.5 3.5v1.3H7.3V3.6H2.7v1.2H0.5z"/><path d="M2 5.5h6l1 3.5H1z"/></svg>
        (555) 019-4482
      </div>
      <div class="contact-item">
        <svg viewBox="0 0 10 10" aria-label="Address"><path d="M5 0.3a3.5 3.5 0 0 1 3.5 3.5C8.5 6.5 5 9.8 5 9.8S1.5 6.5 1.5 3.8A3.5 3.5 0 0 1 5 0.3z"/><circle cx="5" cy="3.8" r="1.3" fill="#fff"/></svg>
        Cedar Bend, OK 73000
      </div>
      <div class="contact-item">
        <svg viewBox="0 0 10 10" aria-label="Website"><circle cx="5" cy="5" r="4.5"/><path d="M0.5 5h9M5 0.5v9M5 0.5c-2.4 2.6-2.4 6.4 0 9M5 0.5c2.4 2.6 2.4 6.4 0 9" stroke="#fff" stroke-width="0.7" fill="none"/></svg>
        www.harlowsrvs.com
      </div>
    </div>
  </section>

</main>
</body>
</html>
```